Newly established winery needs label for its bottles

The Corvel-Tamarin Winery, is a small family owned winery that has been producing wine for little over 3 years. We are now ready to officially start commercializing our products. To do so we are looking for a label for our wine bottles. We are looking for a creative design that will differentiate our bottles from the more conventional labels. We are looking for one label design with 3 color schemes so that we can have a standard look and feel for all three of our wines, while having some differentiation between them with the different color schemes. In summary we are looking for a label that will standout by its uniqueness, simplicity and its modern touch. The label should also reflect the historical significance of the name of the winery. The attached documents offers more detail about the winery, what we are looking for, as well as some technical specification for the label. This label project is also related to a logo project see brief: http://www.pitchvault.ca/project-progress.aspx?briefId=462193). The logo project is now complete and the winning design source files were added to the documents in this brief. Also, details around the information that will need to appear on the label was added to the document list.
Updates
This label project will be on hold temporarily while the logo project is in progress. If you are interested in participating in the logo project, please follow this link: http://www.pitchvault.ca/project-progress.aspx?briefId=462193 Added Wednesday, December 17, 2014
Reason: Deadline extended to give sufficent time for submission and modification to the designs provided.

```html
<!DOCTYPE html>
<html lang="en">
<head>
<meta charset="utf-8">
<title>Corvel-Tamarin Winery – Wine Labels</title>
<link href="https://fonts.googleapis.com/css2?family=Marcellus&family=Crimson+Text:ital@1&display=swap" rel="stylesheet">
<style>
  :root {
    --canvas-bg: #e6e6e1;
    --white-label-bg: #f3f0dc;
    --white-label-ink: #1e1e1e;
    --white-label-frame: #1f1f1f;
    --rose-label-bg: #f5e9ec;
    --rose-label-ink: #6a6265;
    --rose-label-frame: #7a7577;
    --gold: #c9a54a;
    --gold-soft: #e9d7a0;
    --hill-line: #8d8d8d;
  }
  * { box-sizing: border-box; margin: 0; padding: 0; }
  html, body { width: 1200px; height: 953px; overflow: hidden; }
  body {
    background: var(--canvas-bg);
    font-family: "Marcellus", serif;
    position: relative;
  }
  .label {
    position: absolute;
    top: 151px;
    width: 500px;
    height: 650px;
    border: 3px solid var(--frame);
    background: var(--bg);
    color: var(--ink);
  }
  .label--white { left: 60px; --bg: var(--white-label-bg); --ink: var(--white-label-ink); --frame: var(--white-label-frame); }
  .label--rose  { left: 640px; --bg: var(--rose-label-bg); --ink: var(--rose-label-ink); --frame: var(--rose-label-frame); }
  .label__inner-frame {
    position: absolute;
    inset: 10px;
    border: 1px solid var(--frame);
  }
  .label__brand {
    position: absolute;
    top: 90px; left: 0; right: 0;
    display: flex;
    justify-content: center;
    align-items: center;
    gap: 26px;
    font-size: 24px;
    letter-spacing: 0.5px;
  }
  .label__brand-mark {
    width: 54px; height: 54px;
    border-radius: 50%;
    background: var(--gold);
  }
  .label__rule {
    position: absolute;
    top: 232px; left: 125px; right: 125px;
    height: 2px;
    background: linear-gradient(90deg, transparent, var(--gold) 30%, var(--gold-soft) 50%, var(--gold) 70%, transparent);
  }
  .label__title {
    position: absolute;
    top: 252px; left: 0; right: 0;
    text-align: center;
    font-size: 42px;
    letter-spacing: 1px;
  }
  .label__origin {
    position: absolute;
    top: 318px; left: 0; right: 0;
    text-align: center;
    font-size: 18px;
  }
  .label__winery {
    position: absolute;
    top: 368px; left: 0; right: 0;
    text-align: center;
    font-family: "Crimson Text", serif;
    font-style: italic;
    font-size: 17px;
  }
  .label__specs {
    position: absolute;
    top: 478px; left: 40px; right: 40px;
    display: flex;
    justify-content: space-between;
    font-family: "Crimson Text", serif;
    font-style: italic;
    font-size: 16px;
  }
  .label__hills {
    position: absolute;
    left: 11px; right: 11px; bottom: 11px;
    height: 120px;
    background: linear-gradient(180deg, transparent 0%, rgba(141,141,141,0.18) 40%, rgba(141,141,141,0.35) 100%);
    border-top-left-radius: 60% 100%;
    border-top-right-radius: 60% 100%;
  }
</style>
</head>
<body>
  <section class="label label--white" aria-label="White wine label">
    <div class="label__inner-frame"></div>
    <div class="label__brand"><span>CORVEL</span><span class="label__brand-mark"></span><span>TAMARIN</span></div>
    <div class="label__rule"></div>
    <h1 class="label__title">WHITE WINE</h1>
    <p class="label__origin">PRODUCT OF QUÉBEC / PRODUIT DU QUÉBEC</p>
    <p class="label__winery">Winery Corvel-Tamarin / Vignoble Corvel-Tamarin</p>
    <div class="label__specs"><span>750 ml</span><span>11.6% alc./Vol</span></div>
    <div class="label__hills" role="img" aria-label="Line pattern of rolling vineyard hills"></div>
  </section>

  <section class="label label--rose" aria-label="Rosé wine label">
    <div class="label__inner-frame"></div>
    <div class="label__brand"><span>CORVEL</span><span class="label__brand-mark"></span><span>TAMARIN</span></div>
    <div class="label__rule"></div>
    <h1 class="label__title">ROSÉ</h1>
    <p class="label__origin">PRODUCT OF QUÉBEC / PRODUIT DU QUÉBEC</p>
    <p class="label__winery">Winery Corvel-Tamarin / Vignoble Corvel-Tamarin</p>
    <div class="label__specs"><span>750 ml</span><span>11.6% alc./Vol</span></div>
    <div class="label__hills" role="img" aria-label="Line pattern of rolling vineyard hills"></div>
  </section>
</body>
</html>
```